Velmont Hamper company needs a brochure design

We need a brochure design for a new company in Dubai called 'Velmont Hampers'. We already have a logo designed which I have attached and would like to use this and the green/gold/white colours for our brochure. Our company initially will be supplying Velmont Hamper wear of traditional wicker baskets in many designs which hold all the cutlery, crockery and accessories. We will also be selling picnic accessories. We want to purvey a sense of luxury and class in line with our logo. I have attached some photos of the picnicwear. As our products are changing all the time I thought a fold out cover which stays the same and then product cards inserted into the folder which can be changed according to our product changes. I am looking for a fairly simple design and each product card should have at least one photo of the product on it with a spec and description also. On the cover of the folder I would like room to write about the company and what we do, this can be inside or out and may or may not include photos. I have the logo designs in illustrator format and pdf. Please contact if any more information is needed.

Reason: I have extended this deadline as there are some content changes taking place.

```html
<!DOCTYPE html>
<html lang="en">
<head>
<meta charset="utf-8">
<title>Velmont Hampers – Cream Bottle Cooler Product Card</title>
<link rel="stylesheet" href="https://fonts.googleapis.com/css2?family=Montserrat:wght@700&family=Gelasio:wght@400&display=swap">
<style>
  :root {
    --page: #ffffff;
    --forest: #1b321c;
    --gold: #c9a33a;
    --gold-soft: #d8b85a;
    --cream: #f4efe2;
    --copper: #6b2716;
    --product-light: #c9c6bf;
    --product-dark: #8f8b83;
  }
  * { margin: 0; padding: 0; box-sizing: border-box; }
  html, body { width: 1200px; height: 1000px; overflow: hidden; background: var(--page); }
  .canvas { position: relative; width: 1200px; height: 1000px; }

  .card { position: absolute; top: 150px; width: 493px; height: 700px; background: var(--forest); }
  .card--front { left: 100px; }
  .card--back { left: 607px; }

  .heading {
    font-family: "Montserrat", sans-serif; font-weight: 700;
    color: var(--gold); text-transform: uppercase; white-space: nowrap;
  }
  .body-text { font-family: "Gelasio", Georgia, serif; color: var(--cream); }

  .brand-header { position: absolute; left: 0; top: 0; width: 100%; height: 146px; }
  .brand-name {
    position: absolute; left: 0; right: 0; top: 64px; text-align: center;
    font-size: 12px; letter-spacing: 2.6px;
  }

  .foil-band { position: absolute; left: 0; width: 100%; height: 6px; }
  .foil-band--top {
    top: 146px;
    background: linear-gradient(90deg, var(--copper) 0%, #9a5a22 25%, var(--gold) 55%, #fff8e4 77%, var(--gold) 88%, #7a3518 100%);
  }
  .foil-band--bottom {
    top: 513px;
    background: linear-gradient(90deg, #7a3518 0%, var(--gold) 12%, #fff8e4 23%, var(--gold) 45%, #9a5a22 75%, var(--copper) 100%);
  }

  .product-stage { position: absolute; left: 0; top: 152px; width: 100%; height: 361px; background: var(--page); }
  .product-photo {
    position: absolute; left: 192px; top: 38px; width: 106px; height: 292px;
    border-radius: 14px 14px 10px 10px;
    background: linear-gradient(90deg, var(--product-dark) 0%, var(--product-light) 35%, var(--product-light) 60%, var(--product-dark) 100%);
  }

  .product-title { position: absolute; left: 29px; top: 534px; font-size: 23px; letter-spacing: 3.2px; }
  .product-summary { position: absolute; left: 29px; top: 571px; width: 370px; font-size: 10.5px; line-height: 1.3; }

  .web-address {
    position: absolute; left: 0; right: 0; top: 673px; text-align: center;
    font-family: "Gelasio", Georgia, serif; font-size: 10px; color: var(--gold);
  }

  .flourish { position: absolute; left: 218px; width: 58px; height: 18px; background: rgba(201, 163, 58, 0.35); border-radius: 9px; }
  .flourish--top { top: 240px; }
  .flourish--bottom { top: 442px; }
  .rule { position: absolute; left: 180px; width: 133px; height: 1px; background: var(--gold); opacity: 0.8; }
  .rule--top { top: 260px; }
  .rule--bottom { top: 439px; }

  .overview-title { position: absolute; left: 0; right: 0; top: 282px; text-align: center; font-size: 24px; letter-spacing: 3.8px; }
  .overview-subtitle {
    position: absolute; left: 0; right: 0; top: 310px; text-align: center;
    font-family: "Gelasio", Georgia, serif; font-size: 15px; color: var(--gold); letter-spacing: 0.5px;
  }
  .spec-list { position: absolute; left: 102px; top: 349px; width: 300px; list-style: none; font-size: 10.5px; line-height: 16.5px; }
  .spec-list li { position: relative; padding-left: 15px; }
  .spec-list li::before {
    content: ""; position: absolute; left: 1px; top: 6px; width: 6px; height: 5px; background: var(--gold);
  }
</style>
</head>
<body>
<div class="canvas">

  <section class="card card--front">
    <header class="brand-header">
      <p class="brand-name heading">Velmont Hampers</p>
    </header>
    <div class="foil-band foil-band--top"></div>
    <div class="product-stage">
      <div class="product-photo" role="img" aria-label="Photo of the cream insulated bottle cooler duffle with a bottle neck showing at the top"></div>
    </div>
    <div class="foil-band foil-band--bottom"></div>
    <h1 class="product-title heading">Cream Bottle Cooler</h1>
    <p class="product-summary body-text">A stylish cream insulated bottle cooler duffle, perfect for keeping drinks cool for your picnic.</p>
    <p class="web-address">www.velmonthampers.com</p>
  </section>

  <section class="card card--back">
    <div class="flourish flourish--top" role="img" aria-label="Gold scroll ornament"></div>
    <div class="rule rule--top"></div>
    <h2 class="overview-title heading">Cream Bottle Cooler</h2>
    <p class="overview-subtitle">OVERVIEW</p>
    <ul class="spec-list body-text">
      <li>Coordinated Cream Colouring with Velmont Hampers basket range</li>
      <li>Features a water resistant exterior and insulated lining</li>
      <li>Measurements, 100&nbsp; x 300mm</li>
      <li>Made from polyester</li>
    </ul>
    <div class="rule rule--bottom"></div>
    <div class="flourish flourish--bottom" role="img" aria-label="Gold scroll ornament"></div>
    <p class="web-address">www.velmonthampers.com</p>
  </section>

</div>
</body>
</html>
```